Ridgeline comfort mechanical

I want a full wrap other than the top of the van.
My services include hvac central A/C, heat pumps,
Fresh air systems, as well as beer and soda systems, air compressors and cryogenics. I have a 2013 Havrel kd 3400 van high roof

Target Market(s)

Residential and commercial

Industry/Entity Type

HVAC , air compressors, beer and soda systems

Requirements
Nice to have
• Image or design that stands out. Looks sleek and original

```html
<!DOCTYPE html>
<html lang="en">
<head>
<meta charset="utf-8">
<title>Ridgeline Comfort Mechanical – Rear Door Wrap</title>
<link href="https://fonts.googleapis.com/css2?family=Lexend:wght@600;700&family=Montserrat:wght@700&display=swap" rel="stylesheet">
<style>
  :root {
    --backdrop: #22272e;
    --wrap-white: #ffffff;
    --wrap-red: #ec0000;
    --stripe-blue: #3b7be6;
    --navy: #1a1f8f;
    --ink: #111111;
    --trim-grey: #d7dbe0;
    --handle: #3a4049;
    --seam: #c70000;
  }
  * { margin: 0; padding: 0; box-sizing: border-box; }
  html, body {
    width: 1200px; height: 1000px; overflow: hidden;
    background: var(--backdrop);
  }
  .canvas { position: relative; width: 1200px; height: 1000px; }
  .rear-door {
    position: absolute; left: 290px; top: 150px;
    width: 620px; height: 700px;
  }
  .rear-door svg { position: absolute; inset: 0; }
  .brand {
    position: absolute; left: 62px; top: 100px; width: 500px;
    display: flex; align-items: center; gap: 20px;
  }
  .brand-dot {
    flex: none; width: 84px; height: 84px; border-radius: 50%;
    background: var(--navy);
  }
  .brand-text { display: flex; flex-direction: column; }
  .brand-name {
    font-family: "Lexend", sans-serif; font-weight: 700;
    color: var(--navy); font-size: 28px; line-height: 30px;
  }
  .tagline {
    margin-top: 6px;
    font-family: "Montserrat", sans-serif; font-weight: 700;
    color: var(--ink); font-size: 16px; line-height: 20px; letter-spacing: 0.3px;
  }
  .phone {
    position: absolute; left: 0; right: 0; top: 210px; text-align: center;
    font-family: "Lexend", sans-serif; font-weight: 700;
    color: var(--wrap-red); font-size: 40px; line-height: 48px; letter-spacing: 0.5px;
  }
  .services {
    position: absolute; left: 0; right: 0; top: 262px;
    list-style: none; text-align: center;
    font-family: "Lexend", sans-serif; font-weight: 600;
    color: var(--navy); font-size: 20px; line-height: 27px;
  }
  .services li::before { content: "• "; }
</style>
</head>
<body>
<main class="canvas">
  <section class="rear-door">
    <svg width="620" height="700" viewBox="0 0 620 700" aria-hidden="true">
      <defs>
        <clipPath id="door-shape">
          <path d="M60 20 Q310 0 560 20 Q600 30 610 90 L620 600 Q615 680 560 690 L60 690 Q5 680 0 600 L10 90 Q20 30 60 20 Z"/>
        </clipPath>
      </defs>
      <g clip-path="url(#door-shape)">
        <rect class="panel-white" width="620" height="700" fill="var(--wrap-white)"/>
        <path class="panel-red" d="M0 448 Q310 560 620 448 L620 700 L0 700 Z" fill="var(--wrap-red)"/>
        <path class="accent-stripe" d="M0 400 Q310 520 620 400 L620 428 Q310 545 0 428 Z" fill="var(--stripe-blue)"/>
        <path class="window-outline" d="M36 300 L36 88 Q36 68 56 68 L566 68 Q586 68 586 88 L586 300" fill="none" stroke="var(--trim-grey)" stroke-width="2"/>
        <rect class="brake-light" x="254" y="32" width="112" height="18" rx="6" fill="#b0276d"/>
        <rect class="door-handle" x="180" y="516" width="260" height="24" rx="6" fill="var(--handle)"/>
        <circle class="lock" cx="472" cy="526" r="6" fill="#e9e9e9"/>
        <path class="door-seam" d="M40 580 L40 612 Q45 642 80 646 L540 646 Q575 642 580 612 L580 580" fill="none" stroke="var(--seam)" stroke-width="2"/>
      </g>
    </svg>

    <div class="brand">
      <span class="brand-dot"></span>
      <div class="brand-text">
        <span class="brand-name">Ridgeline Comfort<br>Mechanical</span>
        <span class="tagline">BE PROACTIVE NOT REACTIVE</span>
      </div>
    </div>

    <div class="phone">802-555-0147</div>

    <ul class="services">
      <li>Restaurants &amp; Bar Equipment</li>
      <li>Beer &amp; Soda Systems</li>
      <li>Air Compressor/Dryers</li>
      <li>IAQ Testing &amp; Monitoring</li>
      <li>Piping &amp; Heat Pumps</li>
      <li>HVAC Services</li>
      <li>Cryogenics</li>
    </ul>
  </section>
</main>
</body>
</html>
```